BRINTEX Hardware needs a Flyer Designed

We need a flyer designed for a marketing strategy that is to be launched by BRINTEX. As it is for our hardware division, our logo should go unto the flyer. We are offering to our customers financing on items from $5000 up to $35000. Here are some key words that you may want to include; "building or revovating? you pick the job we've got the financing." The flyer should reflect some sort of home construction and should be very attractive and vibrant. On the flyer it should also state that it's "hassle-free" and; "no down payment", "no collateral", "affordable monthly payments".

Must Haves [en ]: The companies logo. Also it must state the address of the company and contact info which is; 47 Fellowby Lane Penal, Trinidad. Tel: 868-47-BRINTEX. Email must also be listed: info@brintexgroup.example.

Nice To Haves [en ]: Good quality graphics. something that is captivating and that will hold the attention of our audience.

Should Not Haves [en ]: Should not be too busy.

Requirements
Must have
• The companies logo. Also it must state the address of the company and contact info which is; 47 Fellowby Lane Penal, Trinidad. Tel: 868-47-BRINTEX. Email must also be listed: info@brintexgroup.example.
Nice to have
• Good quality graphics. something that is captivating and that will hold the attention of our audience.
Should not have
• Should not be too busy.

```html
<!DOCTYPE html>
<html lang="en">
<head>
<meta charset="utf-8">
<title>BRINTEX Hardware – Financing Flyer</title>
<link rel="stylesheet" href="https://fonts.googleapis.com/css2?family=Bebas+Neue&family=Montserrat:wght@600;700;800&display=swap">
<style>
  :root {
    --navy: #1f2c5c;
    --red: #d2192f;
    --red-dark: #b8132a;
    --pink: #f5c9cf;
    --paper: #f1f1f3;
    --paper-2: #e4e5e8;
    --white: #ffffff;
  }
  * { margin: 0; padding: 0; box-sizing: border-box; }
  html, body { width: 950px; height: 1200px; overflow: hidden; background: var(--white); }
  .flyer {
    position: relative; width: 950px; height: 1200px; overflow: hidden;
    background: linear-gradient(180deg, var(--white) 0%, var(--paper) 55%, var(--paper-2) 100%);
    font-family: "Montserrat", sans-serif; color: var(--navy);
  }
  .hero-photo { position: absolute; left: 0; top: 0; }
  .brand {
    position: absolute; right: 35px; top: 60px; width: 350px; text-align: center;
  }
  .brand-name {
    font-family: "Bebas Neue", sans-serif; font-size: 92px; line-height: .9;
    color: var(--navy); letter-spacing: 2px; display: flex; align-items: center; justify-content: center; gap: 10px;
  }
  .brand-dot { width: 22px; height: 22px; background: var(--red); border-radius: 50%; }
  .brand-sub {
    font-size: 11px; font-weight: 700; color: var(--navy); text-align: right;
    border-bottom: 2px solid var(--red); padding-bottom: 3px; margin-top: 2px;
  }
  .brand-group {
    font-size: 13px; font-weight: 600; color: var(--navy); letter-spacing: 1px;
    border-top: 1px solid var(--navy); margin-top: 4px; padding-top: 5px;
  }
  .headline {
    position: absolute; right: 38px; top: 225px; text-align: right;
    font-family: "Bebas Neue", sans-serif; font-weight: 400; line-height: .98;
  }
  .headline-question { font-size: 78px; color: var(--navy); }
  .headline-answer { font-size: 78px; color: var(--red); margin-top: 22px; }
  .offer-band { position: absolute; left: 0; top: 668px; width: 950px; height: 178px; z-index: 1; }
  .offer-text {
    position: absolute; left: 0; top: 670px; width: 950px; height: 176px; text-align: center; z-index: 3;
    display: flex; flex-direction: column; align-items: center; justify-content: center;
  }
  .offer-lead { font-size: 32px; font-weight: 800; line-height: 1.1; }
  .offer-amount { font-family: "Bebas Neue", sans-serif; font-size: 92px; color: var(--red); line-height: .88; }
  .offer-tail { font-size: 42px; font-weight: 800; line-height: 1.1; }
  .city-skyline {
    position: absolute; left: 0; top: 846px; width: 950px; height: 200px; z-index: 0;
    background: linear-gradient(180deg, rgba(200,202,208,.35), rgba(170,173,180,.55));
  }
  .perks { position: absolute; left: 0; top: 866px; width: 950px; display: flex; flex-direction: column; align-items: center; gap: 12px; list-style: none; z-index: 2; }
  .perk {
    border: 2px solid var(--red); border-radius: 22px; padding: 5px 22px;
    font-size: 28px; font-weight: 700; color: var(--navy); background: rgba(255,255,255,.25);
  }
  .contact-bar {
    position: absolute; left: 0; top: 1048px; width: 950px; height: 80px; z-index: 2;
    background: var(--navy); border-top: 5px solid var(--red);
    display: flex; align-items: center; color: var(--white);
  }
  .contact-phone { display: flex; align-items: center; gap: 16px; padding-left: 38px; width: 460px; font-size: 40px; font-weight: 800; }
  .contact-divider { width: 2px; height: 46px; background: rgba(255,255,255,.6); margin-right: 40px; }
  .contact-lines { font-size: 18px; font-weight: 600; line-height: 1.6; }
  .contact-line { display: flex; align-items: center; gap: 14px; }
  .social { position: absolute; left: 0; top: 1128px; width: 950px; height: 72px;
    background: linear-gradient(180deg, #dcdde1, #c9cbd0);
    display: flex; justify-content: center; align-items: center; gap: 8px; font-size: 18px; font-weight: 700; }
  .social-box { width: 26px; height: 26px; border-radius: 4px; }
  .social-box--blue { background: #3b5998; }
  .social-box--red { background: var(--red); }
  .social-box--sky { background: #2aa3d8; }
</style>
</head>
<body>
<main class="flyer">
  <svg class="hero-photo" width="540" height="660" viewBox="0 0 540 660">
    <defs>
      <linearGradient id="buildPhoto" x1="0" y1="0" x2="0" y2="1">
        <stop offset="0" stop-color="#6b7788"/>
        <stop offset=".35" stop-color="#6a5a52"/>
        <stop offset="1" stop-color="#7a4e3e"/>
      </linearGradient>
    </defs>
    <polygon points="300,0 530,330 270,660 0,660 0,0" fill="var(--pink)" opacity=".7"/>
    <polygon points="270,0 478,320 240,640 0,640 0,0" fill="#fff"/>
    <polygon points="262,0 466,320 232,630 0,630 0,0" fill="url(#buildPhoto)" role="img" aria-label="Photo of a high-rise building under construction with a crane against a cloudy sky"/>
  </svg>

  <header class="brand">
    <div class="brand-name"><span class="brand-dot"></span>BRINTEX</div>
    <div class="brand-sub">Brintex Trading Company Limited</div>
    <div class="brand-group">GROUP OF COMPANIES</div>
  </header>

  <h1 class="headline">
    <div class="headline-question">BUILDING OR<br>RENOVATING?</div>
    <div class="headline-answer">YOU PICK THE<br>JOB, WE'VE GOT<br>THE FINANCES!</div>
  </h1>

  <div class="city-skyline" role="img" aria-label="Faded city skyline photo"></div>

  <svg class="offer-band" viewBox="0 0 950 178">
    <polygon points="0,0 190,0 250,178 0,178" fill="var(--red)"/>
    <polygon points="690,0 950,0 950,178 760,178" fill="var(--red-dark)"/>
  </svg>
  <section class="offer-text">
    <div class="offer-lead">GET UP TO</div>
    <div class="offer-amount">$35,000.00</div>
    <div class="offer-tail">HASSLE-FREE AT</div>
  </section>

  <ul class="perks">
    <li class="perk">NO DOWN-PAYMENT</li>
    <li class="perk">NO COLLATERAL</li>
    <li class="perk">AFFORDABLE MONTHLY PAYMENTS</li>
  </ul>

  <footer class="contact-bar">
    <div class="contact-phone">
      <svg width="30" height="30" viewBox="0 0 24 24" fill="none" stroke="#fff" stroke-width="1.6"><path d="M5 3h4l2 5-2.5 1.5a11 11 0 0 0 6 6L16 13l5 2v4a2 2 0 0 1-2 2A17 17 0 0 1 3 5a2 2 0 0 1 2-2z"/></svg>
      868-47-BRINTEX
    </div>
    <div class="contact-divider"></div>
    <div class="contact-lines">
      <div class="contact-line"><svg width="16" height="18" viewBox="0 0 24 24" fill="none" stroke="#fff" stroke-width="2"><path d="M12 22s7-7 7-12a7 7 0 0 0-14 0c0 5 7 12 7 12z"/><circle cx="12" cy="10" r="2.5"/></svg>47 FELLOWBY LANE PENAL, TRINIDAD</div>
      <div class="contact-line"><svg width="18" height="14" viewBox="0 0 24 18" fill="none" stroke="#fff" stroke-width="2"><rect x="1" y="1" width="22" height="16"/><path d="M1 1l11 9 11-9"/></svg>INFO@BRINTEXGROUP.EXAMPLE</div>
    </div>
  </footer>
  <div class="social">FOLLOW US :
    <span class="social-box social-box--blue"></span>
    <span class="social-box social-box--red"></span>
    <span class="social-box social-box--sky"></span>
  </div>
</main>
</body>
</html>
```